WILD COMB label

WILD COMB – Concept Brief

We are designing a label for our premium honey brand, WILD COMB. Our goal is to create a bold, prestigious, and proudly African aesthetic that reflects the product's purity, ethical sourcing, and exceptional quality.

Key Design Elements:

1. Brand Name Emphasis:

The word WILD should be large, bold, eye catching, and prominent, drawing immediate attention.

The word COMB should also be noticeable but doesn’t need to be as dominant as WILD.

2. Visual Theme:

Incorporate African tapestry patterns, ideally within an outline of the African continent or as part of the background design.

The patterns should evoke a sense of tradition, heritage, and authenticity.

3. Text and Messaging:

A clear statement that the honey is:

Natural, raw, Organic Certified, and Ethically Produced.

Sourced from Zambia's pristine Miombo Forests.

Emphasize that this is pure, unadulterated honey of the highest quality.

4. Aesthetic and Impact:

The design should be elegant and prestigious, reinforcing the message that Africa represents quality.

Use rich, earthy tones with bold highlights to ensure the bottle stands out on the shelf and conveys purity and authenticity. Perhaps some use of gold foil in the label or logo.

5. Overall Feel:

The label should exude a sense of luxury while maintaining a strong African identity.

Balancing boldness with elegance will ensure the product feels premium yet natural.

Logo Text

WILD COMB followed by some of the ideas above.

```html
<!DOCTYPE html>
<html lang="en">
<head>
<meta charset="utf-8">
<title>WILD COMB label</title>
<link href="https://fonts.googleapis.com/css2?family=Montserrat:wght@600;700;800&display=swap" rel="stylesheet">
<style>
  :root {
    --backdrop: #1f1a17;
    --cream: #f4e9cf;
    --gold: #e9a935;
    --gold-soft: #f0c565;
    --ink: #120f0d;
    --clay: #c9452b;
    --teal: #4f9a86;
    --sunset-top: #eec7a0;
    --sunset-bottom: #c4482b;
    --pattern-warm: #d8823c;
    --pattern-deep: #b8492f;
  }
  html, body {
    margin: 0;
    padding: 0;
    width: 1198px;
    height: 1200px;
    overflow: hidden;
    background: var(--backdrop);
  }
  .label {
    display: block;
    width: 1198px;
    height: 1200px;
    font-family: "Montserrat", sans-serif;
  }
  .label__base { fill: var(--cream); }
  .label__ring { fill: none; stroke: var(--gold); stroke-width: 4; }
  .label__band--dark { fill: var(--ink); }
  .label__rule { fill: var(--clay); }
  .tapestry__gold { fill: var(--gold); }
  .tapestry__teal { fill: var(--teal); }
  .tapestry__ink { fill: var(--ink); }
  .crest__body { fill: var(--ink); }
  .crest__frame { fill: none; stroke: var(--gold); stroke-width: 7; stroke-linejoin: round; }
  .crest__year { fill: var(--gold); font-weight: 700; font-size: 50px; }
  .crest__map { fill: var(--gold-soft); }
  .brand-word { fill: var(--cream); font-weight: 800; }
  .brand-word--shadow { fill: var(--clay); }
  .crest__claim { fill: var(--cream); font-weight: 700; font-size: 56px; }
  .crest__rule { stroke: var(--clay); stroke-width: 4; }
  .seal__text { fill: var(--cream); font-weight: 700; font-size: 50px; }
  .seal__mark { fill: var(--clay); }
  .origin { fill: var(--ink); font-weight: 700; font-size: 34px; }
</style>
</head>
<body>
<svg class="label" viewBox="0 0 1198 1200" xmlns="http://www.w3.org/2000/svg">
  <defs>
    <clipPath id="label-shape">
      <ellipse cx="600" cy="640" rx="552" ry="615"/>
    </clipPath>
    <linearGradient id="sunset" x1="0" y1="0" x2="0" y2="1">
      <stop offset="0" stop-color="var(--sunset-top)"/>
      <stop offset="1" stop-color="var(--sunset-bottom)"/>
    </linearGradient>
    <linearGradient id="tapestry" x1="0" y1="0" x2="0" y2="1">
      <stop offset="0" stop-color="var(--pattern-warm)"/>
      <stop offset="1" stop-color="var(--pattern-deep)"/>
    </linearGradient>
  </defs>

  <g class="label__body" clip-path="url(#label-shape)">
    <rect class="label__base" x="0" y="0" width="1198" height="1200"/>
    <rect class="label__savanna" role="img" aria-label="Savanna sunset with acacia trees, rhino and giraffe silhouettes" x="0" y="270" width="1198" height="310" fill="url(#sunset)"/>
    <g class="label__tapestry" role="img" aria-label="African tapestry bands of dots and diamond patterns">
      <rect class="tapestry__ink" x="0" y="578" width="1198" height="12"/>
      <rect class="tapestry__gold" x="0" y="590" width="1198" height="30"/>
      <rect class="tapestry__ink" x="0" y="620" width="1198" height="7"/>
      <rect class="tapestry__teal" x="0" y="627" width="1198" height="70"/>
      <rect class="tapestry__ink" x="0" y="697" width="1198" height="8"/>
      <rect class="tapestry__gold" x="0" y="705" width="1198" height="35"/>
      <rect class="tapestry__ink" x="0" y="740" width="1198" height="7"/>
      <rect x="0" y="747" width="1198" height="175" fill="url(#tapestry)"/>
    </g>
    <rect class="label__rule" x="0" y="922" width="1198" height="16"/>
    <rect class="label__band--dark" x="0" y="938" width="1198" height="158"/>
    <rect class="label__rule" x="0" y="1096" width="1198" height="14"/>
    <rect class="label__rule" x="0" y="1186" width="1198" height="14"/>
  </g>
  <ellipse class="label__ring" cx="600" cy="640" rx="528" ry="592"/>

  <g class="crest">
    <polygon class="crest__body" points="598,37 955,349 955,664 598,921 241,664 241,349"/>
    <polygon class="crest__frame" points="598,80 920,362 920,650 598,880 276,650 276,362"/>
    <rect class="crest__map" role="img" aria-label="Outline of the African continent" x="538" y="112" width="118" height="192" rx="34"/>
    <text class="crest__year" x="455" y="292">20</text>
    <text class="crest__year" x="680" y="292">25</text>

    <text class="brand-word brand-word--shadow" x="603" y="516" text-anchor="middle" font-size="205" textLength="520" lengthAdjust="spacingAndGlyphs">WILD</text>
    <text class="brand-word" x="598" y="510" text-anchor="middle" font-size="205" textLength="520" lengthAdjust="spacingAndGlyphs">WILD</text>
    <text class="brand-word brand-word--shadow" x="603" y="662" text-anchor="middle" font-size="170" textLength="520" lengthAdjust="spacingAndGlyphs">COMB</text>
    <text class="brand-word" x="598" y="656" text-anchor="middle" font-size="170" textLength="520" lengthAdjust="spacingAndGlyphs">COMB</text>

    <text class="crest__claim" x="598" y="726" text-anchor="middle">NATURAL</text>
    <line class="crest__rule" x1="448" y1="747" x2="747" y2="747"/>
    <text class="crest__claim" x="598" y="818" text-anchor="middle">RAW</text>
    <line class="crest__rule" x1="556" y1="844" x2="639" y2="844"/>
  </g>

  <g class="seal">
    <text class="seal__text" x="534" y="1000" text-anchor="end">ORGANIC</text>
    <rect class="seal__mark" role="img" aria-label="Small outline of Africa" x="568" y="958" width="40" height="48" rx="10"/>
    <text class="seal__text" x="640" y="1000">CERTIFIED</text>
    <text class="seal__text" x="598" y="1060" text-anchor="middle" textLength="690" lengthAdjust="spacingAndGlyphs">AND ETHICALLY PRODUCED</text>
  </g>

  <text class="origin" x="598" y="1160" text-anchor="middle">PRODUCT OF ZAMBIA</text>
</svg>
</body>
</html>
```